Design flat ui arx 3 inspired app

Know how you fit in the family and how you relate as a family through a shared Tree.
· Keep track of your family as it expands
· Merge family trees or join a common family Tree
· Share family moments by uploading pictures and videos on your calendar
· Get notifications of all events, additions, and other changes to the family tree
· Know where everyone is by keeping in touch through real-time chats
· Share your Tree with friends on social media
· Search for long lost family members and friends
· A great way for your kids to know where they come from

Providing a mobile app that allows users to not only create their family trees but allow them to invite other family members to participate in the completion of the family tree. • User downloads and installs the mobile app, then they proceed to signing up • Signing up the user should provide the following information; profile picture, first name, last name, date of birth, gender, password, email address, country, current city, mobile number • The next step is verifying the mobile number by asking the user to enter the six digit number that was sent to them via sms • Once the mobile number is verified your next step is to enter your family, start with you parents, then spouse(s) or partner(s), then siblings and children if any. This step should be optional, meaning users can skip this step • The app should have a menu bar at the bottom(action bar) with fiver menu items namely, Home, Edit, Tree, Stats, Calendar. • After the user has been signed in their first experience is the home screen, with the profile picture displayed, along with the user’s first name, last name, and age(all the above should be static). Just below all this are three tabs for notifications, photos, and birthdays. • The notifications tab will list all notifications one after the other in text form, example; Kevin updated his high school, Nora added a new member, Brenda has a graduation party coming up, Gordon updated his work experience, Hilda updated her maiden name, Esther updated her siblings, Milton updated his children etc. • Photo’s tab will list all pictures uploaded sorted by latest pictures uploaded and tagged in. One should be able to scroll through the pictures and then when they click on one they can slide though them one after the next viewing them. One should be able to go back to the home screen by clicking the back button. There should be an option to add more photos and share the current ones. • The last tab should be birthdays, which simply lists all birthdays of people who have been entered into the tree from parents to spouses to siblings to children. The birthdays should be listed sorted by month then day, and you should be able to see how old the person is turning. • The next menu bar is the Edit menu which has three tabs namely personal details, family and advanced details. Personal details will have the profile picture, first name, second name, last name, date of birth, gender, twin(if twin then state), relationship status(list spouse if not single), city or place of birth, and living or not. The next tab is the family tab which list and allows you to edit parents, spouse, siblings, and children. The last tab is advanced details, which is hobbies, languages, education, and work experience. • Then the most important part of the app is the Tree function which displays the users family tree, this is all the people added so far and each person is represented by a square with smooth edges, first name and last name displayed first, then age with a green button showing online and a red one showing offline, and below a profile picture. All the relations showed by a line joining the related people. If the person has many spouses they should be stacked together and kids don’t have to show which parent us theirs. One should be able to edit a profile, view a profile, view stats, invite and share. When you invite that person an sms should be generated and the user can enter the mobile number of the family member and once the family members accepts the invitation they then are a member of the tree who can receive notifications on any changes on the tree. Anyone should be able to invite anyone and everyone should see all notifications from everyone who is a member. • The next menu is the statistics menu which displays gender stats, age distribution, birthdays, relationship status, zodiac signs, living vs not living • The last one is the calendar menu which has a calendar where people can add events, upload media, and when a day is clicked and has events on, they should show at the bottom one after the other.

```html
<!DOCTYPE html>
<html lang="en">
<head>
<meta charset="utf-8">
<title>arx 3 Family Tree – App Screens</title>
<link rel="stylesheet" href="https://fonts.googleapis.com/css2?family=Open+Sans:wght@400;600;700&display=swap">
<style>
:root{
  --stage:#5cbf16;
  --lime:#b2f040;
  --lime-soft:#d8f8a8;
  --green:#0ea54b;
  --cyan:#2cc3d6;
  --bar-grey:#6d6970;
  --ink:#3a3a3a;
  --muted:#9a9a9a;
  --line:#d9d9d9;
  --tile:#e3e3e3;
  --photo-a:#7fc3c6;
  --photo-b:#b6dedc;
  --white:#ffffff;
}
*{box-sizing:border-box;margin:0;padding:0}
html,body{width:1200px;height:329px;overflow:hidden}
body{background:var(--stage);font-family:"Open Sans",Arial,sans-serif;color:var(--ink);position:relative}
.screen{position:absolute;top:61px;width:79px;height:140px;background:var(--white);overflow:hidden;font-size:2.6px;line-height:1.25}
.screen.long{height:189px}
.screen.longest{height:246px}
.title-bar{height:7px;background:var(--bar-grey);color:var(--white);font-weight:700;font-size:2.8px;display:flex;align-items:center;justify-content:center}
.app-bar{height:8px;background:var(--lime);display:flex;align-items:center;justify-content:space-between;padding:0 3px}
.app-bar svg{width:4px;height:4px}
.section-title{font-weight:700;text-align:center;font-size:2.8px;margin:3px 0 2px}
.caps{font-weight:700;text-align:center;font-size:2.6px;letter-spacing:.2px;margin:3px 0 2px}
.field{height:5px;border:.3px solid var(--line);margin:1.6px 8px;padding:0 1.5px;color:var(--muted);display:flex;align-items:center;justify-content:space-between}
.field.active{border-color:var(--cyan);color:var(--cyan)}
.underline{border:none;border-bottom:.3px solid var(--line);margin:1.4px 8px;height:5px;color:var(--muted);display:flex;align-items:flex-end;justify-content:space-between;font-size:2.2px}
.toggle{display:flex;gap:.4px}
.toggle i{width:4.5px;height:3.6px;background:var(--cyan);display:block}
.toggle i.off{background:#e6e6e6}
.btn{height:5px;background:var(--green);color:var(--white);font-weight:600;display:flex;align-items:center;justify-content:center;margin:3px 8px}
.avatar-round{width:17px;height:17px;border-radius:50%;margin:3px auto 0;background:radial-gradient(circle at 50% 40%,#f1c9ad,#c98a64 70%,#8c5a3d);border:.6px solid var(--line)}
.hero{height:40px;background:linear-gradient(135deg,var(--photo-a),var(--photo-b));position:relative}
.hero-name{position:absolute;left:0;right:0;bottom:0;height:6px;background:rgba(40,50,50,.55);color:var(--white);display:flex;justify-content:space-between;align-items:center;padding:0 2.5px;font-size:3px}
.tabs3{display:flex;height:8px;border-bottom:.3px solid var(--line)}
.tabs3 span{flex:1;display:flex;align-items:center;justify-content:center}
.tabs3 span.on{background:var(--lime)}
.tabs3 svg{width:3.5px;height:3.5px}
.seg{display:flex;margin:3px 4px;border:.3px solid var(--line)}
.seg span{flex:1;text-align:center;padding:1px 0;font-size:2.2px;color:var(--muted)}
.seg span.on{background:var(--bar-grey);color:var(--white)}
.note{display:flex;align-items:center;gap:2px;padding:2px 3px;border-bottom:.3px solid var(--line);height:10px}
.note .dot{width:5px;height:5px;border-radius:50%;background:linear-gradient(#c89572,#7a5440);flex:none}
.note b{display:block;font-size:2.5px}
.note small{display:block;font-size:1.9px;color:var(--muted)}
.note em{margin-left:auto;font-style:normal;font-size:1.7px;color:var(--muted)}
.nav{position:absolute;left:0;right:0;bottom:0;height:9px;border-top:.3px solid var(--line);display:flex;background:var(--white)}
.nav span{flex:1;display:flex;align-items:center;justify-content:center}
.nav svg{width:4px;height:4px}
.grid{display:grid;grid-template-columns:repeat(4,1fr);gap:1px;padding:1px}
.grid i{display:block;height:10px;background:var(--tile)}
.fab{position:absolute;right:3px;bottom:15px;width:5px;height:5px;background:var(--cyan);color:var(--white);font-size:4px;display:flex;align-items:center;justify-content:center;border-radius:1px}
.box{border:.3px solid var(--line);margin:4px 5px;padding:4px 2px;text-align:center}
.small{font-size:1.9px;color:var(--muted);text-align:center}
.check{display:flex;align-items:center;gap:1px;margin:1px 8px;font-size:2px;color:var(--muted)}
.check i{width:2px;height:2px;border-radius:50%;background:var(--cyan);display:block}
.square-photo{width:18px;height:18px;margin:2px auto 1px;background:linear-gradient(135deg,var(--photo-a),#e8c94a)}
.haze{position:absolute;left:0;right:0;top:8px;height:56px;background:rgba(255,255,255,.55)}
</style>
</head>
<body>

<!-- 1. Profile setup -->
<section class="screen long" style="left:74px">
  <div class="title-bar">Profile Setup</div>
  <div class="avatar-round" role="img" aria-label="Profile photo placeholder"></div>
  <div class="section-title">Personal Details</div>
  <div class="field active">first name</div>
  <div class="field">last name</div>
  <div class="field">Date of birth</div>
  <div class="field" style="border:none">Gender <span class="toggle"><i></i><i class="off"></i></span></div>
  <div class="section-title">Contact Details</div>
  <div class="field">email id</div>
  <div class="field">password</div>
  <div class="field">country <svg viewBox="0 0 6 4" width="4" height="3"><rect width="6" height="4" fill="#c23"/><rect y="1" width="6" height="1" fill="#fff"/><rect y="3" width="6" height=".5" fill="#fff"/><rect width="2.5" height="2" fill="#2b4fa0"/></svg></div>
  <div class="field">current city</div>
  <div class="field" style="justify-content:flex-start;gap:2px"><span style="background:#eee;padding:0 1px">+1</span> mobile number</div>
  <div class="btn" style="margin-top:6px">Next</div>
  <div class="small">Existing user <b style="color:var(--ink)">Log in</b></div>
</section>

<!-- 2. Mobile number verification -->
<section class="screen" style="left:219px">
  <div class="title-bar">Mobile Number Verification</div>
  <div class="box">
    <div style="font-weight:600">Please Check Your Inbox</div>
    <div class="small">We have sent a code to your mobile number</div>
    <div style="margin-top:2px">Enter Your 6 Digit OTP</div>
    <div style="display:flex;justify-content:center;align-items:center;gap:1px;margin-top:2px">
      <span style="border-bottom:.3px solid var(--line);padding:0 2px">654320</span>
      <svg viewBox="0 0 10 10" width="3" height="3"><circle cx="5" cy="5" r="5" fill="var(--green)"/><path d="M3 5l1.5 1.5L7 3.5" stroke="#fff" stroke-width="1.2" fill="none"/></svg>
    </div>
  </div>
  <div class="small" style="margin-top:12px">OTP not Received</div>
  <div style="text-align:center;font-weight:700">Send Again</div>
  <div class="small" style="text-decoration:underline">Need Help</div>
  <div class="check" style="justify-content:center;margin-top:5px"><i style="background:none;border:.3px solid var(--muted)"></i> I accept terms and conditions</div>
  <div class="btn">Next</div>
</section>

<!-- 3. Add loved ones -->
<section class="screen longest" style="left:349px">
  <div class="section-title" style="margin-top:4px">Add your loved ones...</div>
  <div class="caps">PARENTS</div>
  <div class="underline">First Name</div>
  <div class="underline">Last Name</div>
  <div class="underline">D.O.B <span class="toggle">Gender&nbsp;<i></i></span></div>
  <div class="check"><i style="background:none;border:.3px solid var(--muted)"></i> Alive</div>
  <div class="small">Date of Death</div>
  <div class="underline">First Name</div>
  <div class="underline">Last Name</div>
  <div class="underline">D.O.B <span class="toggle">Gender&nbsp;<i></i></span></div>
  <div class="check"><i></i> Alive</div>
  <div class="caps" style="display:flex;justify-content:center;gap:14px;margin-top:6px">SIBLINGS <span>+ −</span></div>
  <div class="underline">First Name</div>
  <div class="underline">Last Name</div>
  <div class="underline">D.O.B <span class="toggle">Gender&nbsp;<i></i></span></div>
  <div class="check"><i></i> Alive</div>
  <div class="small">02</div>
  <div class="underline">First Name</div>
  <div class="underline">Last Name</div>
  <div class="underline">D.O.B <span class="toggle">Gender&nbsp;<i></i></span></div>
  <div class="check"><i></i> Alive</div>
  <div class="btn" style="margin-top:4px">Next</div>
</section>

<!-- 4. Home – notifications -->
<section class="screen" style="left:477px">
  <div class="app-bar"><svg viewBox="0 0 10 10"><path d="M1 2h8M1 5h8M1 8h8" stroke="#fff" stroke-width="1.3"/></svg><svg viewBox="0 0 10 10"><circle cx="4" cy="4" r="3" stroke="#fff" stroke-width="1.2" fill="none"/><path d="M6.5 6.5L9 9" stroke="#fff" stroke-width="1.2"/></svg></div>
  <div class="hero" role="img" aria-label="Profile cover photo of the user"><div class="hero-name"><span>Ray Holden</span><span>24</span></div></div>
  <div class="tabs3">
    <span class="on"><svg viewBox="0 0 10 10"><path d="M5 1a3 3 0 0 1 3 3v3l1 1H1l1-1V4a3 3 0 0 1 3-3z" fill="#fff"/></svg></span>
    <span><svg viewBox="0 0 10 10"><rect x="1" y="2.5" width="8" height="6" rx="1" fill="none" stroke="#999"/><circle cx="5" cy="5.5" r="1.6" fill="none" stroke="#999"/></svg></span>
    <span><svg viewBox="0 0 10 10"><rect x="1" y="4" width="8" height="5" fill="none" stroke="#999"/><path d="M5 1v3" stroke="#999"/></svg></span>
  </div>
  <div class="note"><span class="dot"></span><div><b>Kevin</b><small>updated his high school</small></div><em>2h ago</em></div>
  <div class="note"><span class="dot"></span><div><b>Nora</b><small>added a new member</small></div><em>3h ago</em></div>
  <div class="note"><span class="dot"></span><div><b>Brenda</b><small>has a graduation party coming up</small></div><em>5h ago</em></div>
  <div class="note"><span class="dot"></span><div><b>Gordon</b><small>updated his work experience</small></div><em>1d ago</em></div>
  <nav class="nav">
    <span><svg viewBox="0 0 10 10"><path d="M1 5l4-4 4 4v4H6V6H4v3H1z" fill="var(--green)"/></svg></span>
    <span><svg viewBox="0 0 10 10"><path d="M2 8l1-3 4-4 2 2-4 4z" fill="none" stroke="#aaa"/></svg></span>
    <span><svg viewBox="0 0 10 10"><path d="M5 9V5M5 5L2 1M5 5l3-4" stroke="#aaa" fill="none"/></svg></span>
    <span><svg viewBox="0 0 10 10"><rect x="1.5" y="2" width="7" height="7" fill="none" stroke="#aaa"/><path d="M1.5 4h7" stroke="#aaa"/></svg></span>
    <span><svg viewBox="0 0 10 10"><circle cx="5" cy="5" r="3.5" fill="none" stroke="#aaa"/><path d="M5 2.5V5h2" stroke="#aaa" fill="none"/></svg></span>
  </nav>
</section>

<!-- 5. Edit – family -->
<section class="screen" style="left:603px">
  <div class="app-bar"><svg viewBox="0 0 10 10"><path d="M1 2h8M1 5h8M1 8h8" stroke="#fff" stroke-width="1.3"/></svg><svg viewBox="0 0 10 10"><path d="M2 8l1-3 4-4 2 2-4 4z" stroke="#fff" fill="none"/></svg></div>
  <div class="seg"><span>Personal</span><span class="on">Family</span><span>More</span></div>
  <div class="caps">FATHER</div>
  <div class="underline">First Name <span>Tom</span></div>
  <div class="underline">Last Name <span>Holden</span></div>
  <div class="underline">D.O.B 03.08.1962 <span class="toggle">Gender&nbsp;<i></i></span></div>
  <div class="small" style="text-align:left;margin:1px 8px">Date of Death 01.01.2010</div>
  <div class="caps">MOTHER</div>
  <div class="underline">First Name <span>Ann</span></div>
  <div class="underline">Last Name <span>Holden</span></div>
  <div class="underline">D.O.B 12.05.1965 <span class="toggle">Gender&nbsp;<i></i></span></div>
  <div class="check"><i></i> Alive</div>
  <div class="caps" style="display:flex;justify-content:center;gap:14px">SIBLINGS <span>+ −</span></div>
  <nav class="nav">
    <span><svg viewBox="0 0 10 10"><path d="M1 5l4-4 4 4v4H6V6H4v3H1z" fill="none" stroke="#aaa"/></svg></span>
    <span><svg viewBox="0 0 10 10"><path d="M2 8l1-3 4-4 2 2-4 4z" fill="var(--green)"/></svg></span>
    <span><svg viewBox="0 0 10 10"><path d="M5 9V5M5 5L2 1M5 5l3-4" stroke="#aaa" fill="none"/></svg></span>
    <span><svg viewBox="0 0 10 10"><rect x="1.5" y="2" width="7" height="7" fill="none" stroke="#aaa"/><path d="M1.5 4h7" stroke="#aaa"/></svg></span>
    <span><svg viewBox="0 0 10 10"><circle cx="5" cy="5" r="3.5" fill="none" stroke="#aaa"/><path d="M5 2.5V5h2" stroke="#aaa" fill="none"/></svg></span>
  </nav>
</section>

<!-- 6. Edit – personal -->
<section class="screen" style="left:726px">
  <div class="app-bar"><svg viewBox="0 0 10 10"><path d="M1 2h8M1 5h8M1 8h8" stroke="#fff" stroke-width="1.3"/></svg><svg viewBox="0 0 10 10"><circle cx="4" cy="4" r="3" stroke="#fff" stroke-width="1.2" fill="none"/><path d="M6.5 6.5L9 9" stroke="#fff" stroke-width="1.2"/></svg></div>
  <div class="seg"><span class="on">Personal</span><span>Family</span><span>More</span></div>
  <div class="square-photo" role="img" aria-label="User profile photo"></div>
  <div style="text-align:center;font-size:3px">Ray Holden</div>
  <div class="field active">first name</div>
  <div class="field">second name</div>
  <div class="field">last name</div>
  <div style="display:flex;gap:2px;margin:1.5px 8px;align-items:center"><span class="field" style="margin:0;flex:1">Date of birth</span><span>Gender</span><span class="toggle"><i></i><i class="off"></i></span></div>
  <div style="display:flex;gap:2px;margin:1.5px 8px"><span class="field" style="margin:0;flex:1">Twin ▾</span><span class="field" style="margin:0;flex:1">Relationship</span></div>
  <div class="field">Place of Birth ▾</div>
  <div class="field">Living ▾</div>
  <nav class="nav">
    <span><svg viewBox="0 0 10 10"><path d="M1 5l4-4 4 4v4H6V6H4v3H1z" fill="none" stroke="#aaa"/></svg></span>
    <span><svg viewBox="0 0 10 10"><path d="M2 8l1-3 4-4 2 2-4 4z" fill="var(--green)"/></svg></span>
    <span><svg viewBox="0 0 10 10"><path d="M5 9V5M5 5L2 1M5 5l3-4" stroke="#aaa" fill="none"/></svg></span>
    <span><svg viewBox="0 0 10 10"><rect x="1.5" y="2" width="7" height="7" fill="none" stroke="#aaa"/><path d="M1.5 4h7" stroke="#aaa"/></svg></span>
    <span><svg viewBox="0 0 10 10"><circle cx="5" cy="5" r="3.5" fill="none" stroke="#aaa"/><path d="M5 2.5V5h2" stroke="#aaa" fill="none"/></svg></span>
  </nav>
</section>

<!-- 7. Home – photos -->
<section class="screen" style="left:858px">
  <div class="app-bar"><svg viewBox="0 0 10 10"><path d="M1 2h8M1 5h8M1 8h8" stroke="#fff" stroke-width="1.3"/></svg><svg viewBox="0 0 10 10"><circle cx="4" cy="4" r="3" stroke="#fff" stroke-width="1.2" fill="none"/><path d="M6.5 6.5L9 9" stroke="#fff" stroke-width="1.2"/></svg></div>
  <div class="hero" role="img" aria-label="Profile cover photo of the user"><div class="hero-name"><span>Ray Holden</span><span>24</span></div></div>
  <div class="tabs3">
    <span><svg viewBox="0 0 10 10"><path d="M5 1a3 3 0 0 1 3 3v3l1 1H1l1-1V4a3 3 0 0 1 3-3z" fill="none" stroke="#999"/></svg></span>
    <span class="on"><svg viewBox="0 0 10 10"><rect x="1" y="2.5" width="8" height="6" rx="1" fill="#fff"/><circle cx="5" cy="5.5" r="1.6" fill="var(--lime)"/></svg></span>
    <span><svg viewBox="0 0 10 10"><rect x="1" y="4" width="8" height="5" fill="none" stroke="#999"/><path d="M5 1v3" stroke="#999"/></svg></span>
  </div>
  <div class="grid" role="img" aria-label="Grid of family photos"><i></i><i></i><i></i><i></i><i></i><i></i><i></i><i></i><i></i><i></i><i></i><i></i><i></i><i></i><i></i><i></i></div>
  <div class="fab">+</div>
  <nav class="nav">
    <span><svg viewBox="0 0 10 10"><path d="M1 5l4-4 4 4v4H6V6H4v3H1z" fill="var(--green)"/></svg></span>
    <span><svg viewBox="0 0 10 10"><path d="M2 8l1-3 4-4 2 2-4 4z" fill="none" stroke="#aaa"/></svg></span>
    <span><svg viewBox="0 0 10 10"><path d="M5 9V5M5 5L2 1M5 5l3-4" stroke="#aaa" fill="none"/></svg></span>
    <span><svg viewBox="0 0 10 10"><rect x="1.5" y="2" width="7" height="7" fill="none" stroke="#aaa"/><path d="M1.5 4h7" stroke="#aaa"/></svg></span>
    <span><svg viewBox="0 0 10 10"><circle cx="5" cy="5" r="3.5" fill="none" stroke="#aaa"/><path d="M5 2.5V5h2" stroke="#aaa" fill="none"/></svg></span>
  </nav>
</section>

<!-- 8. Home – photos with edit menu open -->
<section class="screen" style="left:1000px">
  <div class="app-bar"><svg viewBox="0 0 10 10"><path d="M1 2h8M1 5h8M1 8h8" stroke="#fff" stroke-width="1.3"/></svg><svg viewBox="0 0 10 10"><circle cx="4" cy="4" r="3" stroke="#fff" stroke-width="1.2" fill="none"/><path d="M6.5 6.5L9 9" stroke="#fff" stroke-width="1.2"/></svg></div>
  <div class="hero" role="img" aria-label="Profile cover photo of the user"><div class="hero-name"><span>Ray Holden</span><span>24</span></div></div>
  <div class="tabs3">
    <span><svg viewBox="0 0 10 10"><path d="M5 1a3 3 0 0 1 3 3v3l1 1H1l1-1V4a3 3 0 0 1 3-3z" fill="none" stroke="#999"/></svg></span>
    <span class="on"><svg viewBox="0 0 10 10"><rect x="1" y="2.5" width="8" height="6" rx="1" fill="#fff"/><circle cx="5" cy="5.5" r="1.6" fill="var(--lime)"/></svg></span>
    <span><svg viewBox="0 0 10 10"><rect x="1" y="4" width="8" height="5" fill="none" stroke="#999"/><path d="M5 1v3" stroke="#999"/></svg></span>
  </div>
  <div class="grid" role="img" aria-label="Grid of family photos"><i></i><i></i><i></i><i></i><i></i><i></i><i></i><i></i><i></i><i></i><i></i><i></i><i></i><i></i><i></i><i></i></div>
  <div class="haze">
    <div class="seg" style="background:rgba(255,255,255,.6)"><span class="on">Personal</span><span>Family</span><span>More</span></div>
    <div class="small" style="margin-top:34px;display:flex;justify-content:space-around"><span>Add photos</span><span>Share</span></div>
  </div>
  <div class="fab">+</div>
  <nav class="nav">
    <span><svg viewBox="0 0 10 10"><path d="M1 5l4-4 4 4v4H6V6H4v3H1z" fill="var(--green)"/></svg></span>
    <span><svg viewBox="0 0 10 10"><path d="M2 8l1-3 4-4 2 2-4 4z" fill="none" stroke="#aaa"/></svg></span>
    <span><svg viewBox="0 0 10 10"><path d="M5 9V5M5 5L2 1M5 5l3-4" stroke="#aaa" fill="none"/></svg></span>
    <span><svg viewBox="0 0 10 10"><rect x="1.5" y="2" width="7" height="7" fill="none" stroke="#aaa"/><path d="M1.5 4h7" stroke="#aaa"/></svg></span>
    <span><svg viewBox="0 0 10 10"><circle cx="5" cy="5" r="3.5" fill="none" stroke="#aaa"/><path d="M5 2.5V5h2" stroke="#aaa" fill="none"/></svg></span>
  </nav>
</section>

</body>
</html>
```